Business Card Design Competition

We need a business card design for our Internet Marketing company. We require both front and back designs and the final card must be 89x53mm in size, plus crop marks to 91x55mm. Colours as per logo, plus perhaps black and/or grey (#828282).
Final text must be editable (if you can supply an editable Fireworks PNG, even better)...
FRONT TEXT:
Full Name
Position
Address Line
Suburb, State, Postcode
Phone: 0000 000 000
Mobile: 0000 000 000
Email: xxx@brimleafpromo.com.au
Web: www.brimleafpromo.com.au
Rear of card should be a fresh design plus our slogan text: "Getting You Noticed" in large font, then in small text "Brimleaf Holdings Pty Ltd (ABN: 42 563 701 384)".
Target Market(s)
Small/Medium Businesses
Industry/Entity Type
Business
Look and feel
Each slider illustrates characteristics of the customer's brand and the style your logo design should communicate.

```html
<!DOCTYPE html>
<html lang="en">
<head>
<meta charset="utf-8">
<title>Brimleaf Promo – Business Card</title>
<link rel="stylesheet" href="https://fonts.googleapis.com/css2?family=Arimo:wght@400;700&display=swap">
<style>
  :root {
    --backdrop: #5e5a59;
    --card: #ffffff;
    --brand-green: #6bbf2f;
    --brand-orange: #f0901e;
    --text-grey: #4a4a4a;
    --rule-grey: #828282;
  }
  * { margin: 0; padding: 0; box-sizing: border-box; }
  html, body {
    width: 1200px;
    height: 900px;
    overflow: hidden;
    background: var(--backdrop);
    font-family: "Arimo", Arial, sans-serif;
  }
  .canvas {
    position: relative;
    width: 1200px;
    height: 900px;
  }
  .card {
    position: absolute;
    width: 540px;
    height: 322px;
    background: var(--card);
  }
  .card--front { left: 60px; top: 120px; }
  .card--back { left: 600px; top: 458px; }

  .identity {
    position: absolute;
    left: 28px;
    bottom: 58px;
    display: flex;
    align-items: center;
  }
  .brand {
    display: flex;
    align-items: center;
    gap: 10px;
  }
  .brand__dot {
    width: 44px;
    height: 44px;
    border-radius: 50%;
    background: var(--brand-green);
  }
  .brand__name {
    font-size: 20px;
    font-weight: 400;
    color: var(--brand-orange);
    line-height: 1;
  }
  .divider {
    width: 2px;
    height: 52px;
    background: var(--rule-grey);
    margin: 0 12px 0 16px;
  }
  .contact {
    font-size: 11px;
    line-height: 1.3;
    color: var(--text-grey);
  }
  .contact__block + .contact__block { margin-top: 10px; }

  .slogan {
    position: absolute;
    left: 0;
    right: 0;
    top: 128px;
    text-align: center;
    color: var(--brand-green);
  }
  .slogan__line {
    font-size: 40px;
    font-weight: 700;
    letter-spacing: 0.2px;
    line-height: 1;
  }
  .slogan__company {
    margin-top: 6px;
    font-size: 9px;
    font-weight: 700;
  }
</style>
</head>
<body>
<main class="canvas">
  <section class="card card--front" aria-label="Card front">
    <div class="identity">
      <div class="brand">
        <span class="brand__dot" aria-hidden="true"></span>
        <span class="brand__name">Brimleaf Promo</span>
      </div>
      <span class="divider" aria-hidden="true"></span>
      <address class="contact" style="font-style:normal">
        <div class="contact__block">
          123, Sample House, Nr. sample landmark,<br>
          Suburb, Quinsland State. 38001<br>
          Ph. : +6-4512 4512,Mo. +6-451 451 4512
        </div>
        <div class="contact__block">
          xxx@brimleafpromo.com.au<br>
          www.brimleafpromo.com.au
        </div>
      </address>
    </div>
  </section>

  <section class="card card--back" aria-label="Card back">
    <div class="slogan">
      <p class="slogan__line">Getting You Noticed</p>
      <p class="slogan__company">Brimleaf Holdings Pty Ltd (ABN: 42 563 701 384)</p>
    </div>
  </section>
</main>
</body>
</html>
```